Hospital Website Design - PSD only

We need a web design for a community hospital based in Uniontown, Pennsylvania.

We would like to see a first round of designs for the website HOMEPAGE. Once we have selected finalists for the look & feel, based on the submitted homepage designs, we will request an additional INTERNAL page design.

Both designs should follow the content requirements displayed on the attached wireframes. I will post the internal page wireframe after the homepage design finalists are selected.

The desired Look & Feel for the website is clean and modern.

3 sites we like are:
http://www.marvellcare.org/
http://www.qrtm.org/
http://www.dellwyn.org/

Attached are the Homepage wireframe, and the Brackfield Hospital Logo.

The winning design will communicate a bright, healthy, energetic, community-oriented feeling.

Please note that readability is very important for a hospital website. Font-sizes and line-heights should be carefully selected for comfortable reading.
Updates

Dear designers -- Please don't feel locked into the exact shades of blue / brown used in the logo. We find this color scheme quite ugly and are working on a logo update. The new color scheme will probably still involve some shades of blue and brown, but we aren't sure yet. Please use your best judgement to make a beautiful design, similar in style to the modern / simple aesthetic of http://www.marvellcare.org/ We will be working on feedback to designs today. Thank you.

Regarding Large Rotating Graphic area and Navigation: We prefer a full-width display, rather than boxed. The navigation should be visually prominent, easy to read text that one can scan easily across the top of the page. Again, please refer to http://www.marvellcare.org/ for our preferred design aesthetic. Some of the designs submitted have been somewhat dated in their styling. We'd like a polished, modern, crisp, bold, beautiful design.

Re: choice of image in large rotating graphic area -- Designers, please do not use stock photography of a group of doctors, or a nursing home scene, in your sample rotating graphic areas. Although this should not affect our perception of the design, it throws off everything in the page if we don't like the image. Please try to select a bold / attractive image that you would like to set the tone for your design.

Reason: Extending our deadline to receive more designs exploring other color options containing less brown, or browns with a more attractive vibe. We would also like to see designs that are not exact replicas of the wireframe. The wireframe is just to show the elements on the page. Please use your creativity to utilize these elements in an attractive layout that we will like. We would also prefer to see use of photography that shows a younger, more cheerful, hopeful feeling in the design... and where the photographs are consistent with your design approach. Thanks!

In general, feedback for everyone is, please look here: http://www.marvellcare.org/ that's the feeling / vibe we want. DO NOT let the old, ugly, outdated logo determine your design. We are having the logo redesigned. DO NOT take an ugly, outdated template, and adapt it for this website. We want to see something BEAUTIFUL!!! Please give us your best effort! People who come to this website are in health crisis, and they want to be uplifted!! Their good spirits are in your hands.

Reason: We are still reviewing submissions and working with designers to provide better feedback. Thanks for your patience.

Reason: our sincerest apologies for the failure to provide adequate feedback this week. We hit a snag with the various decision makers on this project and were not able to review the recent submissions. We will make every effort to have a decision by tomorrow. Thank you for your patience.

Target Market(s)

Adults based in suburban & rural community, aged 18-80.

Industry/Entity Type

Hospital

Requirements
Must have
• The design must include all of the content areas outlined on the attached wireframe.
The design must include the attached logo. (Note, we may update the logo during the design contest, but it will not be changed dramatically. It will just be modernized slightly.)
Nice to have
• Show hover states for things like Navigation, Links, or small images in gallery, so we can see how you imagine interactive states.

```html
<!DOCTYPE html>
<html lang="en">
<head>
<meta charset="utf-8">
<title>Brackfield Hospital</title>
<link rel="stylesheet" href="https://fonts.googleapis.com/css2?family=Noto+Serif:ital,wght@0,400;0,700;1,400&family=Open+Sans:wght@400;600;700&display=swap">
<style>
:root{
  --navy:#0b1f66;
  --navy-deep:#081a57;
  --blue:#2f64a8;
  --logo-blue:#1f4e9a;
  --grey-text:#666;
  --grey-dark:#444;
  --panel:#dbe3e8;
  --pill:#6d6d6d;
  --tile:#222;
  --rule:#9a9a9a;
  --red:#c8372c;
  --white:#fff;
}
*{box-sizing:border-box;margin:0;padding:0}
html,body{width:1096px;height:1200px;overflow:hidden;background:var(--white)}
body{font-family:"Noto Serif",Georgia,serif;color:var(--grey-dark)}
.page{position:absolute;left:0;top:0;width:1000px;height:1100px;transform:scale(1.096,1.0909);transform-origin:0 0}
.abs{position:absolute}
.topbar{left:0;top:0;width:1000px;height:30px;background:var(--navy)}
.toplinks{left:24px;top:5px;color:var(--white);font-size:16px}
.toplinks span{margin:0 8px;opacity:.8}
.header-curve{left:0;top:30px}
.brand{left:22px;top:80px;display:flex;align-items:center;gap:10px;color:var(--logo-blue);font-size:26px;letter-spacing:.5px}
.brand i{display:block;width:14px;height:14px;background:#7a5630;border-radius:50%}
.call{left:708px;top:4px}
.call-text{left:762px;top:13px;color:var(--white);font-family:"Open Sans",Arial,sans-serif;font-weight:700;font-size:18px}
.search{left:770px;top:48px;width:210px;height:24px;border-radius:12px;background:#d3d3d3;border:1px solid #b5b5b5;font-size:14px;color:#888;padding:2px 16px}
.search b{position:absolute;right:4px;top:3px;width:16px;height:16px;border-radius:50%;background:#eee}
.hero{left:0;top:140px;width:1000px;height:315px;background:linear-gradient(90deg,#c98a6a 0%,#d6a48c 22%,#9bb4c8 42%,#c8d3dd 70%,#d8e0e6 100%)}
.hero-title{left:537px;top:259px;width:350px;height:40px;background:var(--navy);color:var(--white);font-size:32px;line-height:40px;padding-left:18px}
.hero-sub{left:537px;top:309px;width:350px;height:68px;background:var(--white);color:var(--grey-text);font-size:18px;line-height:24px;padding:10px 15px}
.arrow{width:46px;height:46px;border-radius:50%;background:#333;border:2px solid var(--white);color:var(--white);font-size:26px;text-align:center;line-height:40px;font-family:"Open Sans",sans-serif;font-weight:700}
.dots{left:455px;top:423px;display:flex;gap:6px}
.dots i{width:14px;height:14px;border-radius:50%;background:#4a5560}
.dots i.on{background:transparent;border:2px solid var(--white)}
.nav{left:0;top:455px;width:1000px;height:42px;background:var(--navy);display:flex;padding-left:21px}
.nav a{color:var(--white);text-decoration:none;font-size:18px;line-height:42px;padding:0 12px 0 13px}
.nav a.active{background:#d0d0d0;color:var(--navy);padding:0 11px 0 17px}
.quote{left:100px;top:537px;width:800px;text-align:center;font-style:italic;font-size:21px;line-height:31px;color:var(--grey-text)}
.quick{left:19px;top:642px;width:961px;height:88px;background:var(--panel)}
.quick-q{left:42px;top:654px;font-size:16px;color:var(--grey-text)}
.cond{left:41px;top:684px;width:307px;height:30px;border-radius:7px;background:var(--pill);color:#eee;font-size:14px;line-height:30px;padding-left:12px}
.tool{display:flex;align-items:center;gap:8px;font-size:19px;color:var(--grey-text)}
.heading{font-size:20px;color:var(--grey-dark);border-bottom:1px solid var(--rule);padding-bottom:2px}
.thumb{width:104px;height:104px;background:var(--tile)}
.video{left:388px;top:827px;width:341px;height:222px;background:var(--tile)}
.play{left:516px;top:900px;width:84px;height:57px;border-radius:8px;background:#777;border:1px solid #aaa}
.vbar{left:388px;top:1019px;width:341px;height:30px;background:#1a1a1a;border-top:1px solid #333;color:#ddd;font-family:"Open Sans",Arial,sans-serif;font-size:12px}
.more{left:648px;top:1069px;font-size:13px;color:var(--blue)}
.res{left:758px;top:823px;width:225px;list-style:none;font-size:15px;line-height:22px;color:var(--grey-dark)}
.res li{padding-left:14px;text-indent:-14px}
.portal{left:754px;top:978px;width:226px;height:88px;background:#b3d2e6;border:1px solid #8fb0c8}
.portal-title{left:823px;top:982px;font-size:16px;line-height:20px;color:var(--navy-deep)}
.login{left:825px;top:1028px;width:155px;height:29px;background:var(--red);color:var(--white);font-family:"Open Sans",Arial,sans-serif;font-size:16px;line-height:29px;padding-left:4px}
.person{left:758px;top:984px;width:62px;height:78px;background:linear-gradient(#4a7ba8,#2e5a86);border-radius:30px 30px 6px 6px}
</style>
</head>
<body>
<div class="page">
  <div class="abs topbar"></div>
  <div class="abs toplinks">About Us<span>|</span>News<span>|</span>Giving</div>

  <svg class="abs header-curve" width="560" height="170" viewBox="0 0 560 170" aria-hidden="true">
    <path d="M0 0 H552 C520 100 360 170 200 160 C110 155 40 140 0 125 Z" fill="#cdcdcd"/>
    <path d="M0 0 H535 C500 80 360 140 200 135 C110 132 40 125 0 112 Z" fill="#e8e0ea"/>
    <path d="M0 0 H520 C485 70 350 120 200 118 C110 117 40 112 0 100 Z" fill="#f5f5f5"/>
  </svg>
  <div class="abs brand"><i></i>BRACKFIELD HOSPITAL</div>

  <svg class="abs call" width="275" height="48" viewBox="0 0 275 48" aria-hidden="true">
    <path d="M40 8 H260 L272 22 L264 38 H40 Z" fill="var(--blue)"/>
    <circle cx="24" cy="24" r="22" fill="#fff" stroke="#2b2b2b" stroke-width="3"/>
    <path d="M16 14 l5 -2 l4 7 l-3 3 q2 5 6 7 l3 -3 l7 4 l-2 5 q-10 2 -18 -9 q-5 -7 -2 -12 z" fill="#e5702a"/>
  </svg>
  <div class="abs call-text">Call Us (555) 214-3800</div>
  <div class="abs search">search...<b></b></div>

  <div class="abs hero" role="img" aria-label="Photo of a younger hand gently holding an older person's hands, soft blurred clinical background"></div>
  <div class="abs hero-title">Cancer Care Center</div>
  <div class="abs hero-sub">The best doctors and nurses, and treatment close to home.</div>
  <div class="abs arrow" style="left:21px;top:282px">‹</div>
  <div class="abs arrow" style="left:933px;top:282px">›</div>
  <div class="abs dots"><i></i><i></i><i></i><i></i><i class="on"></i></div>

  <nav class="abs nav">
    <a class="active" href="#">Our Services</a>
    <a href="#">Facilities &amp; Directions</a>
    <a href="#">Patient &amp; Visitor Information</a>
    <a href="#">Find a Doctor</a>
    <a href="#">Health &amp; Wellness</a>
  </nav>

  <p class="abs quote">“ Lorem ipsum dolor sit amet, consectetur adipiscing elit. Nunc non diam erat. In fringilla massa ut nisi ullamcorper pellentesque „</p>

  <div class="abs quick"></div>
  <div class="abs quick-q">Do you want to learn about a condition?</div>
  <div class="abs cond">Diabetes, Cancer, Heart Health, ...
    <svg style="position:absolute;right:14px;top:5px" width="22" height="22" viewBox="0 0 22 22" aria-hidden="true"><circle cx="9" cy="9" r="7" fill="none" stroke="#eee" stroke-width="1.5"/><path d="M14 14 L20 20" stroke="#eee" stroke-width="2"/></svg>
  </div>
  <div class="abs tool" style="left:463px;top:653px">
    <svg width="23" height="22" viewBox="0 0 23 22" aria-hidden="true"><rect x="1" y="4" width="21" height="17" rx="2" fill="#555"/><rect x="8" y="1" width="7" height="4" fill="none" stroke="#555" stroke-width="2"/><path d="M11.5 8 v10 M6.5 13 h10" stroke="#fff" stroke-width="3"/></svg>Symptom Checker</div>
  <div class="abs tool" style="left:706px;top:653px">
    <svg width="20" height="20" viewBox="0 0 20 20" aria-hidden="true"><rect x="1" y="3" width="18" height="16" fill="#555"/><path d="M3 8 h14 M3 11 h14 M3 14 h14 M6 8 v9 M10 8 v9 M14 8 v9" stroke="#fff" stroke-width="1"/></svg>Schedule a Lab Test</div>
  <div class="abs tool" style="left:463px;top:694px">
    <svg width="23" height="22" viewBox="0 0 23 22" aria-hidden="true"><rect x="1" y="1" width="21" height="15" fill="#555"/><circle cx="11.5" cy="8.5" r="4" fill="#fff"/><rect x="7" y="17" width="9" height="4" fill="#555"/></svg>Online Bill Pay</div>
  <div class="abs tool" style="left:706px;top:694px">
    <svg width="20" height="22" viewBox="0 0 20 22" aria-hidden="true"><path d="M2 20 L18 3 M2 3 L18 20" stroke="#555" stroke-width="3"/><circle cx="17" cy="3" r="3" fill="#555"/></svg>Support Our Work</div>

  <div class="abs heading" style="left:26px;top:785px;width:699px">Latest Gallery</div>
  <div class="abs thumb" style="left:24px;top:827px"></div>
  <div class="abs thumb" style="left:141px;top:827px"></div>
  <div class="abs thumb" style="left:258px;top:827px"></div>
  <div class="abs thumb" style="left:24px;top:944px"></div>
  <div class="abs thumb" style="left:141px;top:944px"></div>
  <div class="abs thumb" style="left:258px;top:944px"></div>
  <div class="abs video"></div>
  <div class="abs play"><svg width="84" height="57" viewBox="0 0 84 57" aria-hidden="true"><path d="M33 16 L55 28.5 L33 41 Z" fill="#222"/></svg></div>
  <div class="abs vbar">
    <svg style="position:absolute;left:8px;top:8px" width="14" height="14" viewBox="0 0 14 14" aria-hidden="true"><path d="M1 0 L13 7 L1 14 Z" fill="#777"/></svg>
    <span style="position:absolute;left:71px;top:6px">0:00 / 3:55</span>
    <span style="position:absolute;left:150px;top:10px;width:145px;height:8px;background:#000"></span>
    <span style="position:absolute;left:145px;top:6px;width:16px;height:16px;border-radius:50%;background:#ddd"></span>
    <span style="position:absolute;right:8px;top:2px;font-size:18px;color:#777">+</span>
  </div>
  <div class="abs more">VIEW MORE »</div>

  <div class="abs heading" style="left:753px;top:785px;width:226px">Patient Resources</div>
  <ul class="abs res">
    <li>»&nbsp; Tips on Choosing the Right Doctor</li>
    <li>»&nbsp; Billing, Forms, &amp; Medical Records</li>
    <li>»&nbsp; Making the Most of Your Appointment</li>
  </ul>
  <div class="abs portal"></div>
  <div class="abs person" role="img" aria-label="Simple patient silhouette illustration"></div>
  <div class="abs portal-title">BRACKFIELD<br>PATIENT PORTAL</div>
  <div class="abs login">Login or Register &gt;&gt;</div>
</div>
</body>
</html>
```